IT company website design

Require a home page and an inner page designed for a company located in Ohio. The company deals with a wide range of IT services like Software development, IT based education services such as digital textbooks and BPO

Would like to get a Home page for the website and an inner page to be designed.

Design must be modern, clean and very professional. The home page should have a carousel of our services for which content will be provided.

It should give a feel that we are a large company to our prospective customers.
Updates

Hi,
In the few designs I have got for the home page, there are mockups with unwanted content/blocks like ex. latest blog posts or similar blocks. Kindly note that, we don't want this. Please follow the information about content on the home page as mentioned in the project brief. Designers, who have already submitted designs, if you can remove the unwanted blocks, it will be really appreciated.

Thanks.

I have received over 9 designs for this project, but none of them seem to be custom designed for my needs. They are just re-use of previous designs and look very out dated. Looking for fresh, clean designs following latest design trends like the ones you see in gridmarket etc.

If you can provide me a design that meets my expectations, I can definitely UP my budget for you .

Industry/Entity Type

Education

Requirements
Must have
• > > Home page > >
Home page will have

* Top Menu: Home, About Us, Solutions, Services, Contact us (should have space to accommodate for more)

* Should have a flash carousel/slide show. Each slide should be about a service we provide. Ex. a slide for bpo will have the content "Bridging the quality and cost divide in outsourcing" It should be depicted by an illustration or photograph. If you are going to use photograph, please use ones for pixvaultimages.com

* Textual content of about 200 words which we will provide

* Links in the footer along with a copyright, legal notice etc.

* Importantly, the home page should have 2 fancy buttons for "Member Login" and "Online Tutoring"

> > Inner pages > >
Will be mainly textual content explaining each of the service so, should have space for lots of textual content, with a fancy, page title (usually the service name). All inner pages should also have a side menu or something like that from where users can have a one click access to all our services.

Our logo is blue in color. with color code "0080FB". It just a stylized D with rest of the text i.e Varnex Tek Inc. our logo is of the proportion. 1:5 i.e 60px height, 300px wide. We can proportionately increase or decrease the dimensions as necessary. Color combination of the sight should be something that will go with this.

```html
<!DOCTYPE html>
<html lang="en">
<head>
<meta charset="utf-8">
<title>Varnex Tek Inc. — Home</title>
<link href="https://fonts.googleapis.com/css2?family=Aldrich&family=Open+Sans:wght@400;600;700&display=swap" rel="stylesheet">
<style>
:root{
  --page-bg:#f2f2f2;
  --white:#ffffff;
  --brand:#0080fb;
  --heading-blue:#3d8fe0;
  --text-gray:#8a8a8a;
  --nav-gray:#dcdcdc;
  --nav-text:#4a4a4a;
  --nav-active:#6b6b6b;
  --button-blue:#1f7ee8;
  --hero-dark:#020a1c;
  --hero-mid:#0b3a8a;
  --hero-light:#2a7be0;
  --line:#d6d6d6;
  --footer-bg:#e6e6e6;
  --footer-text:#666666;
}
*{margin:0;padding:0;box-sizing:border-box}
html,body{width:1200px;height:879px;overflow:hidden}
body{background:linear-gradient(#e4e4e4,#f4f4f4 110px,var(--page-bg));font-family:"Open Sans",sans-serif;position:relative}
.page{position:absolute;left:28px;top:0;width:1146px;height:879px}
.header{position:absolute;left:0;top:0;width:1146px;height:104px;background:linear-gradient(#f3f3f3,#ececec)}
.logo-tab{position:absolute;left:24px;top:54px;width:242px;height:50px;background:var(--white);border:1px solid var(--line);border-bottom:none;border-radius:6px 6px 0 0;box-shadow:0 -1px 3px rgba(0,0,0,.08)}
.logo-name{position:absolute;left:16px;top:9px;font-family:"Open Sans",sans-serif;font-weight:600;font-size:27px;color:var(--brand);white-space:nowrap;letter-spacing:-.3px}
.action-bar{position:absolute;left:781px;top:52px;width:365px;height:39px;background:linear-gradient(#f8f8f8,#e2e2e2);border:1px solid #cfcfcf;border-radius:6px}
.action-arrow{position:absolute;left:0;top:0}
.action-btn{position:absolute;top:8px;height:22px;background:linear-gradient(#3a95f0,var(--button-blue));color:var(--white);font-weight:700;font-size:11px;line-height:22px;text-align:center;border:1px solid #1768c4}
.btn-tutoring{left:135px;width:109px}
.btn-login{left:250px;width:108px}
.main-nav{position:absolute;left:0;top:104px;width:1146px;height:32px;background:linear-gradient(#e6e6e6,#d2d2d2);border-top:1px solid #c4c4c4}
.main-nav a{position:absolute;top:4px;height:23px;line-height:23px;font-size:14px;font-weight:700;color:var(--nav-text);text-decoration:none;padding:0 14px}
.main-nav a.active{background:var(--nav-active);color:var(--white)}
.hero{position:absolute;left:0;top:136px;width:1146px;height:326px;background:radial-gradient(ellipse at 70% 40%,var(--hero-light) 0%,var(--hero-mid) 35%,var(--hero-dark) 80%)}
.hero-title{position:absolute;left:35px;top:99px;font-family:"Aldrich",sans-serif;font-size:40px;color:#e8ecf2;white-space:nowrap;letter-spacing:.5px}
.hero-text{position:absolute;left:34px;width:1100px;color:var(--white);font-weight:700;font-size:12.4px;line-height:15.6px}
.hero-text.first{top:181px}
.hero-text.second{top:228px}
.hero-foot{position:absolute;left:0;top:462px;width:1146px;height:26px;background:linear-gradient(#d8d8d8,#f6f6f6)}
.content{position:absolute;left:0;top:488px;width:1146px;height:359px;background:var(--white)}
.intro{position:absolute;left:26px;top:20px;width:432px}
.intro h1{font-size:19.5px;font-weight:700;color:var(--heading-blue);white-space:nowrap;letter-spacing:-.2px}
.intro p{margin-top:23px;font-size:12.4px;font-weight:700;color:var(--text-gray);line-height:17.8px}
.intro p + p{margin-top:17px}
.feature{position:absolute;left:478px;width:355px;height:149px;background:var(--white);border:1px solid #e2e2e2;border-radius:6px;box-shadow:0 1px 4px rgba(0,0,0,.12)}
.feature.one{top:22px}
.feature.two{top:181px}
.feature-thumb{position:absolute;left:22px;top:46px;width:60px;height:48px;border-radius:3px}
.feature.one .feature-thumb{background:linear-gradient(#cfd3d8,#4a4f58)}
.feature.two .feature-thumb{background:linear-gradient(#3a5a8a,#12233f)}
.feature h2{position:absolute;left:98px;top:13px;width:240px;font-size:13px;font-weight:700;color:var(--heading-blue);line-height:13.5px}
.feature p{position:absolute;left:98px;top:48px;width:240px;font-size:10px;font-weight:600;color:var(--text-gray);line-height:14px}
.video{position:absolute;left:851px;top:21px;width:260px;height:152px;border-radius:8px;background:linear-gradient(#3a3d42,#0c0d0f 60%,#2a2c30)}
.signup{position:absolute;left:858px;top:184px;width:250px}
.signup h3{text-align:center;font-size:13.5px;font-weight:700;color:var(--heading-blue)}
.email-field{position:absolute;left:0;top:20px;width:207px;height:29px;border:1px solid var(--line);border-radius:3px;text-align:center;line-height:27px;font-size:14px;color:#c4c4c4}
.go-btn{position:absolute;left:213px;top:19px;width:35px;height:29px;background:linear-gradient(#2f8cec,#1467c9);border-radius:3px;color:var(--white);font-weight:700;font-size:18px;line-height:29px;text-align:center}
.social{position:absolute;left:0;width:249px;height:30px;border:1px solid var(--line);border-radius:3px}
.social .mark{position:absolute;left:13px;top:4px;width:21px;height:21px;border-radius:3px}
.social span{position:absolute;left:42px;right:0;top:0;text-align:center;line-height:28px;font-size:14px;color:#c0c0c0}
.social.s1{top:56px}.social.s1 .mark{background:#3b5998}
.social.s2{top:89px}.social.s2 .mark{background:#3aa0d8}
.social.s3{top:122px}.social.s3 .mark{background:#e8811c}
.footer{position:absolute;left:0;top:847px;width:1146px;height:32px;background:var(--footer-bg);font-family:Arial,sans-serif;font-size:9.2px;color:var(--footer-text)}
.copyright{position:absolute;left:41px;top:12px}
.footer-links{position:absolute;right:32px;top:11px}
.footer-links a{color:var(--footer-text);text-decoration:none;padding:0 3px;border-left:1px solid #555}
.footer-links a:first-child{border-left:none}
</style>
</head>
<body>
<div class="page">
  <header class="header">
    <div class="logo-tab"><span class="logo-name">Varnex Tek Inc.</span></div>
    <div class="action-bar">
      <svg class="action-arrow" width="78" height="39" viewBox="0 0 78 39" aria-hidden="true">
        <defs><linearGradient id="arrowFill" x1="0" y1="0" x2="0" y2="1"><stop offset="0" stop-color="#5aa6f2"/><stop offset="1" stop-color="#1560c0"/></linearGradient></defs>
        <path d="M0 10 H50 V1 L74 19.5 L50 38 V29 H0 Z" fill="url(#arrowFill)"/>
      </svg>
      <a class="action-btn btn-tutoring">Online Tutoring</a>
      <a class="action-btn btn-login">Member Login</a>
    </div>
  </header>

  <nav class="main-nav">
    <a class="active" style="left:282px">Home</a>
    <a style="left:363px">About Us</a>
    <a style="left:468px">Solutions</a>
    <a style="left:573px">Services</a>
    <a style="left:668px">Contact Us</a>
  </nav>

  <section class="hero" role="img" aria-label="Slide photograph of glowing blue fibre-optic light strands">
    <h2 class="hero-title">Bridging the quality and cost divide in outsourcing</h2>
    <p class="hero-text first">Quisque vitae pede. Nam et augue. Sed a elit. Ut vel massa. Suspendisse nibh pede ultrices vitae, ultrices nec, mollis non nibh.Quisque vitae pede. Nam et augue. Sed a elit Ut vel massa. Suspendisse nibh pede, ultrices vitae,ultrices nec mollis non nibh</p>
    <p class="hero-text second">Quisque vitae pede. Nam etaugue. Sed a elit. Ut vel massa. Suspendisse nibh pede ultrices vitae ultrices nec, mollis non nibh. Quisque vitae pede. Nam et ugue. Sed a elit. Ut vel massa. Suspendisse nibh pede, ultrices vitae ultrices nec, molli non nibh... Quisque vitae pede. Nam et augue. Sed a elit. Ut vel massa. Suspendisse nibh pede, ultrices vitae ultrices nec, mollis non nibh...Suspendisse nibh pede, ultrices vitae ultrices nec, mollis non nibh... Quisque vitae pede. Nam etaugue. Sed a elit. Ut vel massa. Suspendisse nibh pede ultrices vitae ultrices nec, mollis non nibh.</p>
  </section>
  <div class="hero-foot"></div>

  <main class="content">
    <article class="intro">
      <h1>Cras neque justo rhoncus a facilisis eget , nisl.</h1>
      <p>Cras neque justo, ultrices at, rhoncus a facilisiseget,nisl. Quisque vitae pede. Nam et augue. Sed a elit. Ut vel massa. Suspendisse nibh pede, ultrices vitae, ultrices nec, mollis non nibh. In sit amet pedequis leo vulputate&nbsp; hendrerit. Craslaoreet leo et justo auctor condimentum. Integer id enim. Suspendisse nibh pede, ultrices vitae, ultrices nec, mollis non, nibh. In sit&nbsp; amet pede quis leo vulputate hendrerit. Suspendisse nibh pede, ultrices vitae, ultrices nec, mollis non nibh.</p>
      <p>In sit amet pede quis leo vulputate&nbsp; hendrerit. Cras laoreet leo et justo auctor condimentum. Integer id enim. In sit amet pede quis leo vulputate&nbsp; hendrerit. Cras laoreet leo et justo auctor condimentum. Integer id enim.</p>
    </article>

    <div class="feature one">
      <div class="feature-thumb" role="img" aria-label="Desktop computer monitor"></div>
      <h2>Cras neque justo, ultrices at, rhoncus a facilisis eget nisl.</h2>
      <p>Cras neque justo, ultrices at, rhoncus a facilisis eget,nisl. Quisque vitae&nbsp; pede. Nam et augue. Sed a elit. Ut vel massa. Suspendisse nibh pede, ultrices vitae, ultrices nec, mollis non nibh.</p>
    </div>
    <div class="feature two">
      <div class="feature-thumb" role="img" aria-label="Close-up of keyboard keys"></div>
      <h2>Cras neque justo, ultrices at, rhoncus a facilisis eget nisl.</h2>
      <p>Cras neque justo, ultrices at, rhoncus a facilisis eget,nisl. Quisque vitae&nbsp; pede. Nam et augue. Sed a elit. Ut vel massa. Suspendisse nibh pede, ultrices vitae, ultrices nec, mollis non nibh.</p>
    </div>

    <div class="video" role="img" aria-label="Video player showing a laptop with a play button"></div>

    <aside class="signup">
      <h3>eNews sign up</h3>
      <div class="email-field">Your email</div>
      <div class="go-btn">Go</div>
      <div class="social s1"><i class="mark"></i><span>like us on Linkbook</span></div>
      <div class="social s2"><i class="mark"></i><span>follow us on Chirper</span></div>
      <div class="social s3"><i class="mark"></i><span>subscribe to rss feed</span></div>
    </aside>
  </main>

  <footer class="footer">
    <span class="copyright">Copyright© 2011 All rights reserved</span>
    <nav class="footer-links"><a>Contact us</a><a>Terms and Conditions</a><a>Site map</a></nav>
  </footer>
</div>
</body>
</html>
```